A.I. Software PowerPoint Presentation

We need a PowerPoint presentation design for our artificial intelligence product qvPilot.

We've attached our current PowerPoint to use as a base. This presentation is used to introduce and describe what the product is, how it works, why you need it, what makes it better than other solutions, and how to implement it.

We would like the PowerPoint design to be more professional-looking as we present to executives and CIOs of banks, government, and other large corporations. We are a tech startup and would like the design to convey the feel of innovation and high-tech, but also trustworthy, reputable, and capable, for the more conservative audiences.

The PowerPoint should have minimal use of animation (animate only if necessary). It should be modern and clean and not too busy.

We appreciate design work on all of the following: slide backgrounds, title slide, fonts, pictures used in the slides, layout, charts, graphics, comparison versus, etc. If you have any ideas for the slide contents, please also provide any suggestions/recommendations.

I've also attached our qvPilot logo if that is needed, as well as our brochure.

We look forward to your submissions!

EDIT:
I would like to add that we are using PowerPoint 2010 on a PC (.pptx file), and that the slides should be in 16:9 mainly but also with 4:3 version (if possible cut off the sides and squish in the content a little, no need to make a new set of slides) as sometimes we cannot control whose projector we are presenting on. Thanks

Target Market(s)

Enterprise clients, multi-national corporations,
banks, airlines, telecommunications, government

Industry/Entity Type

Software

Font styles to use
Serif
Sans Serif

Colors

Designer to choose colors to be used in the design.

Requirements
Nice to have
• Professional, clean-look, modern design
Should not have
• Should not look cheesy (i.e. tons of stock photos, business cliche pictures)
• Should not look over-done/over-the-top
• Should not look outdated

```html
<!DOCTYPE html>
<html lang="en">
<head>
<meta charset="utf-8">
<title>qvPilot Presentation Slides</title>
<link href="https://fonts.googleapis.com/css2?family=Raleway:wght@300;400;600;700&display=swap" rel="stylesheet">
<style>
:root{
  --blue:#1aa9e8;
  --blue-light:#3cc0f2;
  --blue-deep:#1a6fc9;
  --ink:#232629;
  --grey:#b9bcbf;
  --text:#9a9ea3;
  --panel:#1fa4dc;
  --bg:#ffffff;
}
*{margin:0;padding:0;box-sizing:border-box}
html,body{width:1200px;height:1110px;overflow:hidden;background:var(--bg);font-family:'Raleway',sans-serif}
.slide{position:absolute;width:384px;height:216px;background:#fff;overflow:hidden;box-shadow:0 1px 4px rgba(0,0,0,.22)}
.abs{position:absolute}
.title{position:absolute;left:16px;top:12px;font-size:17px;font-weight:300;color:var(--blue);white-space:nowrap}
.title::after{content:"";display:block;width:26px;height:1.5px;background:var(--blue);margin-top:3px}
.logo{position:absolute;right:14px;top:10px;display:flex;align-items:center;gap:3px;font-size:11px;font-weight:400;color:var(--blue)}
.logo i{width:12px;height:12px;border-radius:50%;background:var(--blue);display:block}
.logo.white{color:#fff}.logo.white i{background:#fff}
.foot{position:absolute;left:5px;bottom:4px;font-size:3.6px;color:var(--blue)}
.pg{position:absolute;right:0;bottom:0;width:14px;height:14px;background:var(--blue);clip-path:polygon(100% 0,100% 100%,0 100%)}
.pg span{position:absolute;right:2px;bottom:2px;font-size:3.5px;color:#fff}
.lead{position:absolute;font-size:9px;color:var(--blue);line-height:1.3}
.t{font-size:5px;line-height:1.4;color:var(--text)}
.t p+p{margin-top:6px}
.h{font-size:8.5px;color:var(--blue);margin-bottom:3px}
.hs{font-size:6px;color:var(--blue);margin-bottom:1px}
.hs.dark{color:var(--ink)}
.ic{width:14px;height:14px;border-radius:50%;background:var(--blue);position:relative;flex:none}
.ic.abs{position:absolute}
.ic::after{content:"";position:absolute;left:50%;top:50%;width:5px;height:5px;margin:-2.5px 0 0 -2.5px;border-radius:50%;border:1px solid #fff}
.ic.deep{background:var(--blue-deep)}.ic.dark{background:var(--ink)}
.ic.ring{background:#fff;border:1px solid var(--blue)}.ic.ring::after{border-color:var(--blue)}
.ic.ring.dark{border-color:var(--ink)}.ic.ring.dark::after{border-color:var(--ink)}
.bullet{position:absolute;display:flex;gap:6px;width:112px}
.center{text-align:center}
</style>
</head>
<body>

<!-- Row 1 -->
<section class="slide" style="left:8px;top:0">
  <div class="title">Three Column Description</div>
  <div class="logo"><i></i>qvPilot</div>
  <div class="lead" style="left:20px;top:52px;width:330px">This is place for your header text. Insert your text here, just replace this text with your own text</div>
  <div class="abs t" style="left:20px;top:87px;width:100px"><p>Our platform reads data from every source and turns it into clear, timely answers your teams can act on with full confidence.</p><p>Built for secure, regulated work and large, complex teams.</p></div>
  <div class="abs t" style="left:143px;top:87px;width:100px"><p>Models learn from your own workflows and improve with each task, saving hours of manual review every single week.</p><p>Deploy on premises or in a private cloud of your choice.</p></div>
  <div class="abs t" style="left:266px;top:87px;width:100px"><p>Every decision is logged and fully traceable, so audits stay simple and compliance teams keep full control of results.</p><p>Scale from one team to the whole enterprise with ease.</p></div>
  <div class="foot">© 2017 qvPilot All rights reserved</div><div class="pg"><span>16</span></div>
</section>

<section class="slide" style="left:408px;top:0">
  <div class="abs" role="img" aria-label="Abstract blue technology light streaks" style="left:0;top:0;width:228px;height:216px;background:radial-gradient(ellipse at 45% 45%,#7ab8e6 0%,#2a5b9c 35%,#0b1a3a 75%,#050a18 100%)"></div>
  <div class="abs" style="left:228px;top:0;width:156px;height:216px;background:var(--panel)"></div>
  <div class="logo white" style="left:246px;right:auto;top:32px;font-size:15px;gap:5px"><i style="width:17px;height:17px"></i>qvPilot</div>
  <div class="abs" style="left:246px;top:72px;display:flex;gap:14px">
    <span style="width:22px;height:22px;border:1.2px solid #fff;border-radius:50%;display:block"></span>
    <span style="width:22px;height:22px;border:1.2px solid #fff;border-radius:50%;display:block"></span>
    <span style="width:22px;height:22px;border:1.2px solid #fff;border-radius:50%;display:block"></span>
  </div>
  <div class="abs" style="left:244px;top:119px;font-size:15px;font-weight:300;color:#fff;line-height:1.05">Your Title<br>Goes Here</div>
  <div class="abs t" style="left:244px;top:155px;width:128px;color:#e6f6fd">A short line that introduces the product and frames the main idea of this talk for the room.</div>
  <div class="abs" style="left:228px;top:197px;width:156px;height:19px;background:#1896d0;color:#fff;font-size:5.5px;text-align:center;line-height:19px">www.qvpilot-demo.net</div>
</section>

<section class="slide" style="left:808px;top:0">
  <div class="title">Your Title Goes Here</div>
  <div class="logo"><i></i>qvPilot</div>
  <div class="abs" style="left:16px;top:46px;width:355px"><div class="hs">Heading Goes Here</div><div class="t">A short summary of the services we offer and how each one helps large teams reach faster, safer and clearer decisions across the business.</div></div>
  <div class="bullet" style="left:16px;top:80px;width:150px"><div class="ic"></div><div><div class="hs">Service Number One</div><div class="t">Short line about this service and the value it brings to the client team.</div></div></div>
  <div class="bullet" style="left:16px;top:116px;width:150px"><div class="ic deep"></div><div><div class="hs">Service Number Two</div><div class="t">Short line about this service and the value it brings to the client team.</div></div></div>
  <div class="bullet" style="left:16px;top:152px;width:150px"><div class="ic dark"></div><div><div class="hs dark">Service Number Three</div><div class="t">Short line about this service and the value it brings to the client team.</div></div></div>
  <div class="abs" style="left:200px;top:78px;width:168px;height:30px;background:var(--blue);display:flex;align-items:center;color:#fff"><b style="font-size:20px;font-weight:400;width:26px;text-align:center;border-right:1.5px solid #fff;line-height:20px">1</b><span class="t" style="color:#fff;padding-left:8px">A clear point that supports the first service in a few short words.</span></div>
  <div class="abs" style="left:200px;top:114px;width:168px;height:30px;background:var(--blue-deep);display:flex;align-items:center;color:#fff"><b style="font-size:20px;font-weight:400;width:26px;text-align:center;border-right:1.5px solid #fff;line-height:20px">2</b><span class="t" style="color:#fff;padding-left:8px">A clear point that supports the second service in a few short words.</span></div>
  <div class="abs" style="left:200px;top:150px;width:168px;height:30px;background:var(--ink);display:flex;align-items:center;color:#fff"><b style="font-size:20px;font-weight:400;width:26px;text-align:center;border-right:1.5px solid #fff;line-height:20px">3</b><span class="t" style="color:#fff;padding-left:8px">A clear point that supports the third service in a few short words.</span></div>
  <div class="foot">© 2017 qvPilot All rights reserved</div><div class="pg"><span>18</span></div>
</section>

<!-- Row 2 -->
<section class="slide" style="left:8px;top:224px">
  <div class="title">Four Bullets with Paragraph</div>
  <div class="logo"><i></i>qvPilot</div>
  <div class="bullet" style="left:24px;top:70px;width:82px"><div class="ic"></div><div><div class="hs">Your Text Here</div><div class="t">Short note on this point for the slide.</div></div></div>
  <div class="bullet" style="left:110px;top:70px;width:82px"><div class="ic"></div><div><div class="hs">Your Text Here</div><div class="t">Short note on this point for the slide.</div></div></div>
  <div class="bullet" style="left:24px;top:132px;width:82px"><div class="ic"></div><div><div class="hs">Your Text Here</div><div class="t">Short note on this point for the slide.</div></div></div>
  <div class="bullet" style="left:110px;top:132px;width:82px"><div class="ic"></div><div><div class="hs">Your Text Here</div><div class="t">Short note on this point for the slide.</div></div></div>
  <div class="abs t" style="left:210px;top:70px;width:160px"><div class="h">Heading Goes Here</div><p>The platform connects to your systems in days and brings every team onto one shared view of the data.</p><p>Results are clear, traced and easy to explain to any board.</p><p>Support is ready at every stage of the rollout.</p></div>
  <div class="foot">© 2017 qvPilot All rights reserved</div><div class="pg"><span>19</span></div>
</section>

<section class="slide" style="left:408px;top:224px">
  <div class="title">Your Title</div>
  <div class="logo"><i></i>qvPilot</div>
  <div class="abs t" style="left:15px;top:64px;width:100px"><div class="h">Heading Goes Here</div><p>A short paragraph that explains the main idea of this slide in plain words.</p><p>One more line that adds some detail.</p><p>A final note to close the thought for the audience.</p></div>
  <div class="abs" role="img" aria-label="Chrome humanoid robot figure" style="left:138px;top:0;width:112px;height:216px;background:linear-gradient(100deg,#cfd5db 0%,#7d8893 45%,#3b434b 100%);border-radius:40px 40px 0 0"></div>
  <div class="bullet" style="left:272px;top:62px"><div class="ic"></div><div><div class="hs">Your Text Here</div><div class="t">Short note on this point.</div></div></div>
  <div class="bullet" style="left:272px;top:94px"><div class="ic"></div><div><div class="hs">Your Text Here</div><div class="t">Short note on this point.</div></div></div>
  <div class="bullet" style="left:272px;top:125px"><div class="ic"></div><div><div class="hs">Your Text Here</div><div class="t">Short note on this point.</div></div></div>
  <div class="bullet" style="left:272px;top:157px"><div class="ic"></div><div><div class="hs">Your Text Here</div><div class="t">Short note on this point.</div></div></div>
  <div class="foot">© 2017 qvPilot All rights reserved</div><div class="pg"><span>20</span></div>
</section>

<section class="slide" style="left:808px;top:224px">
  <div class="title">Text &amp; Bullet Area</div>
  <div class="logo"><i></i>qvPilot</div>
  <div class="abs t" style="left:18px;top:60px;width:100px"><div class="h">Heading Goes Here</div><p>A short paragraph that explains the main idea of this slide in plain words.</p><p>One more line that adds some detail.</p><p>A final note to close the thought.</p></div>
  <div class="bullet" style="left:150px;top:60px"><div class="ic"></div><div><div class="hs">Your Text Here</div><div class="t">Short note on this point for you.</div></div></div>
  <div class="bullet" style="left:150px;top:92px"><div class="ic"></div><div><div class="hs">Your Text Here</div><div class="t">Short note on this point for you.</div></div></div>
  <div class="bullet" style="left:150px;top:123px"><div class="ic"></div><div><div class="hs">Your Text Here</div><div class="t">Short note on this point for you.</div></div></div>
  <div class="bullet" style="left:150px;top:154px"><div class="ic"></div><div><div class="hs">Your Text Here</div><div class="t">Short note on this point for you.</div></div></div>
  <div class="bullet" style="left:270px;top:60px"><div class="ic"></div><div><div class="hs">Your Text Here</div><div class="t">Short note on this point for you.</div></div></div>
  <div class="bullet" style="left:270px;top:92px"><div class="ic"></div><div><div class="hs">Your Text Here</div><div class="t">Short note on this point for you.</div></div></div>
  <div class="bullet" style="left:270px;top:123px"><div class="ic"></div><div><div class="hs">Your Text Here</div><div class="t">Short note on this point for you.</div></div></div>
  <div class="bullet" style="left:270px;top:154px"><div class="ic"></div><div><div class="hs">Your Text Here</div><div class="t">Short note on this point for you.</div></div></div>
  <div class="foot">© 2017 qvPilot All rights reserved</div><div class="pg"><span>21</span></div>
</section>

<!-- Row 3 -->
<section class="slide" style="left:8px;top:446px">
  <div class="abs" role="img" aria-label="Glass walkway bridge under a blue tint" style="inset:0;background:linear-gradient(135deg,#38bdf0 0%,#1fa6e0 50%,#1690cb 100%)"></div>
  <div class="logo white" style="top:16px;right:14px;font-size:14px;gap:5px"><i style="width:16px;height:16px"></i>qvPilot</div>
  <div class="abs" style="left:0;top:108px;width:202px;text-align:center;color:#fff">
    <div style="font-size:6.5px">Divider Page</div>
    <div style="font-size:17px;font-weight:700;margin-top:2px">Your Title Goes Here</div>
    <div style="font-size:8px;font-weight:300;margin-top:2px">Your Subtitle Here</div>
  </div>
</section>

<section class="slide" style="left:408px;top:446px">
  <div class="title">Paragraph with Three Bullet</div>
  <div class="logo"><i></i>qvPilot</div>
  <div class="lead" style="left:18px;top:56px;width:330px">This is place for your header text. Insert your text here, just replace this text with your own text</div>
  <div class="abs t" style="left:19px;top:97px;width:118px"><p>A short paragraph that sets the context for the three points on the right and links them together for the reader.</p><p>One more line that adds the detail the audience needs.</p></div>
  <div class="abs" style="left:136px;top:95px;width:1px;height:98px;background:#dfe2e4"></div>
  <div class="abs t center" style="left:152px;top:92px;width:62px"><div class="ic ring" style="margin:0 auto 5px;width:20px;height:20px"></div><div class="hs">Your Text Here</div><p>Short note on this point.</p><p>One more line here.</p></div>
  <div class="abs t center" style="left:228px;top:92px;width:62px"><div class="ic ring" style="margin:0 auto 5px;width:20px;height:20px"></div><div class="hs">Your Text Here</div><p>Short note on this point.</p><p>One more line here.</p></div>
  <div class="abs t center" style="left:305px;top:92px;width:62px"><div class="ic ring dark" style="margin:0 auto 5px;width:20px;height:20px"></div><div class="hs dark">Your Text Here</div><p>Short note on this point.</p><p>One more line here.</p></div>
  <div class="foot">© 2017 qvPilot All rights reserved</div><div class="pg"><span>23</span></div>
</section>

<section class="slide" style="left:808px;top:446px">
  <div class="title">Global Experience</div>
  <div class="logo"><i></i>qvPilot</div>
  <div class="abs" role="img" aria-label="World map with office locations" style="left:95px;top:44px;width:235px;height:128px;background:#d3d6d9;border-radius:30px 40px 50px 30px"></div>
  <div class="abs" style="left:17px;top:163px;display:flex;align-items:center;gap:4px"><span style="width:12px;height:12px;border-radius:50%;background:var(--blue);display:block"></span><span class="hs" style="margin:0">Heading Goes Here</span></div>
  <div class="abs t" style="left:17px;top:178px;width:200px">A short line about our offices and the clients we serve in every region.</div>
  <div class="foot">© 2017 qvPilot All rights reserved</div><div class="pg"><span>24</span></div>
</section>

<!-- Row 4 -->
<section class="slide" style="left:8px;top:668px">
  <div class="title">Global Experience</div>
  <div class="logo"><i></i>qvPilot</div>
  <div class="abs" role="img" aria-label="United States map with highlighted states" style="left:22px;top:48px;width:240px;height:140px;background:linear-gradient(90deg,#1a8bd8 0%,#d3d6d9 25%,#d3d6d9 100%);border-radius:10px 40px 30px 20px"></div>
  <div class="abs" style="left:268px;top:148px;width:105px"><div class="hs">Content Title</div><div class="t" style="color:#555">A short line about this region and the clients we serve there.</div></div>
  <div class="foot">© 2017 qvPilot All rights reserved</div><div class="pg"><span>25</span></div>
</section>

<section class="slide" style="left:408px;top:668px">
  <div class="title">Multiple Column Area</div>
  <div class="logo"><i></i>qvPilot</div>
  <div class="abs t center" style="left:20px;top:58px;width:56px"><div class="ic" style="margin:0 auto 4px"></div><div class="hs">Your Text Here</div>Short note on this point.</div>
  <div class="abs t center" style="left:91px;top:58px;width:56px"><div class="ic deep" style="margin:0 auto 4px"></div><div class="hs">Your Text Here</div>Short note on this point.</div>
  <div class="abs t center" style="left:162px;top:58px;width:56px"><div class="ic dark" style="margin:0 auto 4px"></div><div class="hs dark">Your Text Here</div>Short note on this point.</div>
  <div class="abs t center" style="left:233px;top:58px;width:56px"><div class="ic" style="margin:0 auto 4px"></div><div class="hs">Your Text Here</div>Short note on this point.</div>
  <div class="abs t center" style="left:304px;top:58px;width:56px"><div class="ic" style="margin:0 auto 4px"></div><div class="hs">Your Text Here</div>Short note on this point.</div>
  <div class="abs" style="left:28px;top:113px;width:328px;height:1px;background:#dfe2e4"></div>
  <div class="abs t" style="left:27px;top:130px;width:150px"><div class="h">Heading Goes Here</div><p>A short paragraph that explains this column and the idea it covers for the audience.</p><p>One more line that adds a little detail.</p></div>
  <div class="abs t" style="left:207px;top:130px;width:150px"><div class="h">Heading Goes Here</div><p>A short paragraph that explains this column and the idea it covers for the audience.</p><p>One more line that adds a little detail.</p></div>
  <div class="foot">© 2017 qvPilot All rights reserved</div><div class="pg"><span>26</span></div>
</section>

<section class="slide" style="left:808px;top:668px">
  <div class="title">Your Pie Chart Area</div>
  <div class="logo"><i></i>qvPilot</div>
  <svg class="abs" style="left:0;top:0" width="384" height="216" viewBox="0 0 384 216">
    <g fill="none" stroke-width="5">
      <circle cx="58" cy="96" r="18" stroke="#d9dbdd"/><circle cx="58" cy="96" r="18" stroke="#1aa9e8" stroke-dasharray="22.6 113.1" transform="rotate(-90 58 96)"/>
      <circle cx="147" cy="96" r="18" stroke="#d9dbdd"/><circle cx="147" cy="96" r="18" stroke="#1a6fc9" stroke-dasharray="56.5 113.1" transform="rotate(-90 147 96)"/>
      <circle cx="236" cy="96" r="18" stroke="#d9dbdd"/><circle cx="236" cy="96" r="18" stroke="#232629" stroke-dasharray="79.2 113.1" transform="rotate(-90 236 96)"/>
      <circle cx="325" cy="96" r="18" stroke="#d9dbdd"/><circle cx="325" cy="96" r="18" stroke="#8f9499" stroke-dasharray="33.9 113.1" transform="rotate(-90 325 96)"/>
    </g>
    <g font-family="Raleway, sans-serif" font-size="10" text-anchor="middle" font-weight="300">
      <text x="58" y="100" fill="#1aa9e8">20%</text><text x="147" y="100" fill="#1a6fc9">50%</text>
      <text x="236" y="100" fill="#232629">70%</text><text x="325" y="100" fill="#555">30%</text>
    </g>
  </svg>
  <div class="abs t center" style="left:26px;top:124px;width:64px"><div style="font-size:4.5px;font-weight:700;color:var(--blue)">Subtitle in this area</div>A short note that explains this share in a line.</div>
  <div class="abs t center" style="left:115px;top:124px;width:64px"><div style="font-size:4.5px;font-weight:700;color:var(--blue-deep)">Subtitle in this area</div>A short note that explains this share in a line.</div>
  <div class="abs t center" style="left:204px;top:124px;width:64px"><div style="font-size:4.5px;font-weight:700;color:var(--ink)">Subtitle in this area</div>A short note that explains this share in a line.</div>
  <div class="abs t center" style="left:293px;top:124px;width:64px"><div style="font-size:4.5px;font-weight:700;color:var(--ink)">Subtitle in this area</div>A short note that explains this share in a line.</div>
  <div class="foot">© 2017 qvPilot All rights reserved</div><div class="pg"><span>27</span></div>
</section>

<!-- Row 5 -->
<section class="slide" style="left:8px;top:891px">
  <div class="title">Your Pie Chart Area</div>
  <div class="logo"><i></i>qvPilot</div>
  <svg class="abs" style="left:0;top:0" width="384" height="216" viewBox="0 0 384 216">
    <g fill="none" stroke-width="20" transform="rotate(-126 200 110)">
      <circle cx="200" cy="110" r="30" stroke="#3cc0f2" stroke-dasharray="37.7 188.5"/>
      <circle cx="200" cy="110" r="30" stroke="#1a8fd8" stroke-dasharray="0 37.7 52.8 188.5"/>
      <circle cx="200" cy="110" r="30" stroke="#232629" stroke-dasharray="0 90.5 51.3 188.5"/>
      <circle cx="200" cy="110" r="30" stroke="#3b4046" stroke-dasharray="0 141.8 46.7 188.5"/>
    </g>
    <g font-family="Raleway, sans-serif" font-size="7.5" font-weight="700" fill="#fff" text-anchor="middle">
      <text x="200" y="88">20%</text><text x="229" y="108">35%</text><text x="186" y="138">40%</text><text x="172" y="101">30%</text>
    </g>
  </svg>
  <div class="abs t" style="left:62px;top:66px;width:56px;text-align:right"><div style="font-size:4.5px;font-weight:700;color:var(--blue)">Secure</div>Short note on this point here.</div>
  <div class="ic ring abs" style="left:124px;top:66px;width:22px;height:22px;border-width:1.2px"></div>
  <div class="abs t" style="left:62px;top:134px;width:56px;text-align:right"><div style="font-size:4.5px;font-weight:700;color:var(--ink)">Good Package</div>Short note on this point here.</div>
  <div class="ic dark abs" style="left:124px;top:134px;width:22px;height:22px"></div>
  <div class="ic deep abs" style="left:254px;top:66px;width:22px;height:22px"></div>
  <div class="abs t" style="left:282px;top:66px;width:60px"><div style="font-size:4.5px;font-weight:700;color:var(--blue-deep)">Well Organized</div>Short note on this point here.</div>
  <div class="ic dark abs" style="left:254px;top:134px;width:22px;height:22px"></div>
  <div class="abs t" style="left:282px;top:134px;width:60px"><div style="font-size:4.5px;font-weight:700;color:var(--ink)">Publication</div>Short note on this point here.</div>
  <div class="abs t center" style="left:60px;top:180px;width:264px">A short closing line that sums up what the chart shows and why the split matters for the plan ahead this year.</div>
  <div class="foot">© 2017 qvPilot All rights reserved</div><div class="pg"><span>28</span></div>
</section>

<section class="slide" style="left:408px;top:891px">
  <div class="title">Your Pie Chart Area</div>
  <div class="logo"><i></i>qvPilot</div>
  <svg class="abs" style="left:0;top:0" width="384" height="216" viewBox="0 0 384 216">
    <path d="M52 78 v12 a68 26 0 0 0 136 0 v-12 z" fill="#1584c4"/>
    <ellipse cx="120" cy="78" rx="68" ry="26" fill="#1ab2ee"/>
    <path d="M120 78 L64 63 A68 26 0 0 1 150 55 Z" fill="#232629"/>
    <path d="M120 78 L52 78 A68 26 0 0 1 64 63 Z" fill="#1a6fc9"/>
    <path d="M52 78 A68 26 0 0 0 90 101 L96 110 A68 26 0 0 1 52 90 Z" fill="#15579e"/>
    <g font-family="Raleway, sans-serif" font-size="3.5" fill="#9a9ea3">
      <circle cx="91" cy="135" r="1.2" fill="#1aa9e8"/><text x="94" y="136.3">Sales A</text>
      <circle cx="110" cy="135" r="1.2" fill="#1a6fc9"/><text x="113" y="136.3">Sales B</text>
      <circle cx="129" cy="135" r="1.2" fill="#232629"/><text x="132" y="136.3">Sales C</text>
    </g>
  </svg>
  <div class="bullet" style="left:240px;top:60px;width:130px"><div class="ic"></div><div><div class="hs">Your Text Here</div><div class="t">Short note on this point.</div></div></div>
  <div class="bullet" style="left:240px;top:87px;width:130px"><div class="ic deep"></div><div><div class="hs">Your Text Here</div><div class="t">Short note on this point.</div></div></div>
  <div class="bullet" style="left:240px;top:114px;width:130px"><div class="ic dark"></div><div><div class="hs dark">Your Text Here</div><div class="t">Short note on this point.</div></div></div>
  <div class="abs" style="left:24px;top:150px;font-size:15px;font-weight:700;color:var(--blue-deep)">▲54%</div>
  <div class="abs t" style="left:79px;top:150px;width:240px"><div class="hs">Heading Goes Here</div>A short paragraph on growth this period and what drove the strong result across the main client groups we serve today.</div>
  <div class="foot">© 2017 qvPilot All rights reserved</div><div class="pg"><span>29</span></div>
</section>

<section class="slide" style="left:808px;top:891px">
  <div class="abs" role="img" aria-label="Blue digital code texture" style="inset:0;background:linear-gradient(160deg,#1b8fc4 0%,#1a7fb4 50%,#1c98cf 100%)"></div>
  <svg class="abs" style="left:0;top:0" width="384" height="216" viewBox="0 0 384 216">
    <polygon points="150,0 330,0 292,216 122,216" fill="#5fc6ee"/>
    <polygon points="162,0 330,0 292,216 136,216" fill="#ffffff"/>
  </svg>
  <div class="logo" style="left:150px;right:auto;top:126px;font-size:16px;gap:4px"><i style="width:17px;height:17px"></i>qvPilot</div>
  <div class="abs" style="left:148px;top:148px;width:184px;text-align:center;font-size:15px;font-weight:300;color:var(--blue)">Divider Page</div>
  <div class="abs" style="left:148px;top:168px;width:184px;text-align:center;font-size:7px;color:var(--blue)">Your Subtitle Here</div>
</section>

</body>
</html>
```